Engineering Consultant Business Card

I'm starting a new business as a high-end engineering consultant in a niche field. I've attached the jpg for my logo plus the branding guideline document that I've been following. You can see my business website here: www.orvalink.com
I'd like a business card that has the logo on one side, then the other side has (in any order): Tessmor Pact, Inc.
Delia Whitcombe
President and Chief EMC Engineer
www.orvalink.com
delia@orvalink.com
Optional: motto "We will solve your EMC problems as early as possible—ideally before they even start."
I'm not planning on including a phone number
Target Market(s)
Businesses, especially makers of electronics hardware
Industry/Entity Type
Electrical engineering
Contact Information for Business Card
Company name, my name, website, email
Look and feel
Each slider illustrates characteristics of the customer's brand and the style your logo design should communicate.

```html
<!DOCTYPE html>
<html lang="en">
<head>
<meta charset="utf-8">
<title>Delia Whitcombe – Business Card</title>
<link href="https://fonts.googleapis.com/css2?family=Fira+Sans+Condensed:wght@400;600&display=swap" rel="stylesheet">
<style>
  :root {
    --backdrop: #222222;
    --card-white: #f4f5f8;
    --brand-blue: #2a4a9e;
    --brand-blue-light: #6f8fd8;
    --ink: #1c1c22;
    --rule: #3a3a44;
  }
  * { margin: 0; padding: 0; box-sizing: border-box; }
  html, body {
    width: 1200px; height: 780px; overflow: hidden;
    background: var(--backdrop);
    font-family: "Fira Sans Condensed", sans-serif;
  }
  .canvas {
    position: relative; width: 1200px; height: 780px;
    display: flex; align-items: center; justify-content: center; gap: 60px;
  }
  .card {
    position: relative; width: 520px; height: 300px;
    box-shadow: 0 14px 30px rgba(0,0,0,.45);
  }
  .card-front { background: var(--card-white); color: var(--ink); }
  .card-back {
    background: var(--brand-blue);
    display: flex; align-items: center; justify-content: center;
  }

  .identity { position: absolute; left: 34px; top: 40px; }
  .identity-name {
    font-weight: 600; font-size: 34px; line-height: 1;
    color: var(--brand-blue); letter-spacing: -.3px;
  }
  .identity-title { font-size: 15px; margin-top: 6px; }

  .divider {
    position: absolute; left: 262px; top: 112px;
    width: 1px; height: 92px; background: var(--rule);
  }

  .contact { position: absolute; left: 284px; top: 132px; list-style: none; }
  .contact-item {
    display: flex; align-items: center; gap: 8px;
    font-size: 16px; line-height: 1.55;
  }
  .contact-icon { width: 14px; height: 14px; flex: none; }

  .motto {
    position: absolute; left: 34px; right: 30px; bottom: 30px;
    font-size: 15.5px;
  }

  .mark { display: flex; align-items: center; gap: 14px; }
  .mark-dot {
    width: 26px; height: 26px; border-radius: 50%;
    border: 3px solid var(--brand-blue-light);
  }
  .mark-name {
    font-weight: 600; font-size: 40px; letter-spacing: .5px;
    color: var(--brand-blue-light);
  }
</style>
</head>
<body>
<main class="canvas">
  <section class="card card-front" aria-label="Business card front">
    <div class="identity">
      <h1 class="identity-name">Delia Whitcombe</h1>
      <p class="identity-title">President and Chief EMC Engineer</p>
    </div>
    <div class="divider"></div>
    <ul class="contact">
      <li class="contact-item">
        <svg class="contact-icon" viewBox="0 0 14 14" aria-hidden="true">
          <circle cx="7" cy="7" r="6" fill="none" stroke="#2a4a9e" stroke-width="1.6"/>
          <ellipse cx="7" cy="7" rx="2.6" ry="6" fill="none" stroke="#2a4a9e" stroke-width="1.2"/>
          <line x1="1" y1="7" x2="13" y2="7" stroke="#2a4a9e" stroke-width="1.2"/>
        </svg>
        www.orvalink.com
      </li>
      <li class="contact-item">
        <svg class="contact-icon" viewBox="0 0 14 14" aria-hidden="true">
          <rect x="1" y="3" width="12" height="8.5" rx="1" fill="#2a4a9e"/>
          <polyline points="1.5,3.6 7,8 12.5,3.6" fill="none" stroke="#f4f5f8" stroke-width="1.2"/>
        </svg>
        delia@orvalink.com
      </li>
    </ul>
    <p class="motto">We will solve your EMC problems as early as possible—ideally before they even start</p>
  </section>

  <section class="card card-back" aria-label="Business card back">
    <div class="mark">
      <span class="mark-dot"></span>
      <span class="mark-name">Tessmor Pact</span>
    </div>
  </section>
</main>
</body>
</html>
```